Financial Service Company Need Business Card Design

This is a new startup company, first of its kind to offer this service. We facilitate the movement of deposit funds electronically between home buyers and real estate brokerages.Our customers are REALTORS®, real estate brokerages, and home buyers, we identify ourselves as a financial/technology company.
Not looking for anything too flashy. Just a clean design that shows the logo, contact info, etc. Company colors can be seen on attached logo, and 'coming soon page'
www.plumvault.ca
Industry/Entity Type
Business
Contact Information for Business Card

```html
<!DOCTYPE html>
<html lang="en">
<head>
<meta charset="utf-8">
<title>PlumVault Business Card</title>
<link href="https://fonts.googleapis.com/css2?family=Montserrat:wght@400;500;600&display=swap" rel="stylesheet">
<style>
  :root {
    --orange: #e2582a;
    --charcoal: #3d3d3d;
    --logo-grey: #5a5a5a;
    --card-light: #f4f4f4;
    --card-mid: #dcdcdc;
    --white: #ffffff;
    --page: #ffffff;
  }
  * { box-sizing: border-box; margin: 0; padding: 0; }
  html, body {
    width: 1200px; height: 620px; overflow: hidden;
    background: var(--page);
    font-family: "Montserrat", sans-serif;
  }
  .canvas { position: relative; width: 1200px; height: 620px; }

  .card {
    position: absolute;
    background: linear-gradient(160deg, var(--white) 0%, var(--card-light) 45%, var(--card-mid) 100%);
    border: 1px solid #cfcfcf;
    box-shadow: 0 1px 3px rgba(0,0,0,0.25);
    overflow: hidden;
  }

  /* Front */
  .card-front { left: 68px; top: 28px; width: 345px; height: 203px; }
  .wordmark {
    position: absolute; display: flex; align-items: center; gap: 9px;
    color: var(--logo-grey); font-weight: 500; letter-spacing: -0.5px;
    white-space: nowrap;
  }
  .wordmark .mark { background: var(--orange); flex: none; }
  .card-front .wordmark { left: 44px; top: 62px; font-size: 36px; }
  .card-front .wordmark .mark { width: 30px; height: 30px; }
  .tagline {
    position: absolute; left: 45px; top: 134px; width: 255px; height: 22px;
    border-top: 1px solid var(--orange); border-bottom: 1px solid var(--orange);
    font-size: 9.4px; color: var(--charcoal); text-align: center; line-height: 20px;
    white-space: nowrap;
  }

  /* Back */
  .card-back { left: 145px; top: 242px; width: 202px; height: 347px; }
  .card-back .wordmark { left: 17px; top: 27px; font-size: 21px; gap: 6px; }
  .card-back .wordmark .mark { width: 18px; height: 18px; }
  .band { position: absolute; left: 0; width: 100%; }
  .band-name { top: 58px; height: 58px; background: var(--orange); color: var(--white); text-align: right; padding: 19px 18px 0 0; }
  .band-name .person { font-size: 15px; font-weight: 500; line-height: 1; }
  .band-name .role { font-size: 8px; color: var(--charcoal); font-weight: 600; }
  .band-phones { top: 116px; height: 87px; background: var(--charcoal); padding: 5px 0 0 44px; }
  .phone-row { display: flex; align-items: center; gap: 8px; height: 26px; color: var(--white); font-size: 14px; font-weight: 500; white-space: nowrap; }
  .phone-row svg { width: 19px; height: 19px; flex: none; }
  .band-email { top: 205px; height: 19px; background: var(--white); display: flex; align-items: center; padding-left: 27px; gap: 6px; font-size: 11px; color: var(--charcoal); white-space: nowrap; }
  .band-email svg { width: 11px; height: 9px; flex: none; }
  .band-address { top: 226px; height: 75px; background: var(--orange); color: var(--white); text-align: center; font-size: 10px; font-weight: 500; line-height: 12.8px; padding-top: 7px; font-style: normal; }
  .band-web { top: 303px; height: 25px; background: var(--charcoal); color: var(--white); text-align: center; font-size: 12.5px; line-height: 25px; font-weight: 500; }
</style>
</head>
<body>
<main class="canvas">

  <section class="card card-front" aria-label="Business card front">
    <div class="wordmark"><span class="mark"></span>PlumVault</div>
    <p class="tagline">Secure Digital Deposits for Every Home Purchase</p>
  </section>

  <section class="card card-back" aria-label="Business card back">
    <div class="wordmark"><span class="mark"></span>PlumVault</div>

    <div class="band band-name">
      <p class="person">Alan Marsh</p>
      <p class="role">CEO</p>
    </div>

    <div class="band band-phones">
      <p class="phone-row">
        <svg viewBox="0 0 20 20" aria-hidden="true"><circle cx="10" cy="10" r="9.5" fill="#6a6a6a"/><path d="M6.5 5.5l2 0 1 2.5-1.2 1a6 6 0 0 0 2.7 2.7l1-1.2 2.5 1v2a1 1 0 0 1-1 1A8 8 0 0 1 5.5 6.5a1 1 0 0 1 1-1z" fill="#fff"/></svg>
        0412 908 3361
      </p>
      <p class="phone-row">
        <svg viewBox="0 0 20 20" aria-hidden="true"><circle cx="10" cy="10" r="9.5" fill="#6a6a6a"/><rect x="7" y="4.5" width="6" height="11" rx="1" fill="none" stroke="#fff" stroke-width="1.2"/><circle cx="10" cy="13.6" r="0.7" fill="#fff"/></svg>
        0412 557 2049
      </p>
      <p class="phone-row">
        <svg viewBox="0 0 20 20" aria-hidden="true"><circle cx="10" cy="10" r="9.5" fill="#6a6a6a"/><rect x="5.5" y="8" width="9" height="7" rx="1" fill="#fff"/><rect x="7.5" y="4.5" width="5" height="4" fill="none" stroke="#fff" stroke-width="1"/><rect x="7" y="10" width="6" height="1" fill="#6a6a6a"/><rect x="7" y="12" width="6" height="1" fill="#6a6a6a"/></svg>
        0198 740 2253
      </p>
    </div>

    <div class="band band-email">
      <svg viewBox="0 0 11 9" aria-hidden="true"><rect x="0.5" y="0.5" width="10" height="8" fill="none" stroke="#3d3d3d"/><path d="M0.5 0.5l5 4.5 5-4.5" fill="none" stroke="#3d3d3d"/></svg>
      info@alanmarsh.com.au
    </div>

    <address class="band band-address">
      88 Harlow Street<br>CityName<br>StateName<br>Canada<br>K2P 4R7
    </address>

    <div class="band band-web">www.plumvault.ca</div>
  </section>

</main>
</body>
</html>
```